Business Cards and stationery for Land (Real Estate) Development Group
Torvik Group, Land Development and Consulting
Business Cards and stationery  for Land (Real Estate) Development Group - Real Estate
Creative Brief
Professional
Marcus Pellowe
418 West Orchard Ave, Suite 312 Brenham, TX 77561
marcusp@torvikgroup.example
I would like to see designs consisting of either double sided standard sized Business Card [3.5" x 2"] or double sided rounded corner business card 3.35 x 2.2 Let's see if the words "we bring land to life" can be added somewhere on the card - or maybe on the back Also, please provide layouts for stationary as well If the logo, or a portion of the logo, can be placed on the back of the card along with the slogan that would be great.
We bring land to life.
Zentro Zentro
Ok. Can u give some star rating please.
marcusp marcusp
Please feel free to use the "D" logo separately from the text "Torvik Group" if a necessary for a design. Also, separate the tagline if you as the designer feel like it should be larger, etc. Also, please let me see options of business cards with rounded corners as well. Thanks.

```html
<!DOCTYPE html>
<html lang="en">
<head>
<meta charset="utf-8">
<title>Torvik Group – Business Card</title>
<link rel="stylesheet" href="https://fonts.googleapis.com/css2?family=Exo+2:wght@400;500;600&display=swap">
<style>
  :root {
    --backdrop: #e6e7e9;
    --card: #ffffff;
    --green: #1f6b3b;
    --navy: #22437f;
    --ink: #3b3d42;
    --muted: #55585e;
  }
  * { box-sizing: border-box; margin: 0; padding: 0; }
  html, body { width: 1200px; height: 816px; overflow: hidden; }
  body {
    background: var(--backdrop);
    font-family: "Exo 2", Arial, sans-serif;
    color: var(--ink);
    position: relative;
  }
  .card {
    position: absolute;
    left: 120px; top: 93px;
    width: 960px; height: 630px;
    background: var(--card);
    border-radius: 44px;
    box-shadow: 0 10px 30px rgba(0,0,0,.12);
  }
  .holder {
    position: absolute; left: 60px; top: 122px;
    display: flex; align-items: center; gap: 20px;
  }
  .holder-icon { width: 56px; height: 56px; }
  .holder-name { font-size: 27px; font-weight: 500; letter-spacing: 1.5px; text-transform: uppercase; color: var(--ink); line-height: 1.1; white-space: nowrap; }
  .holder-title { font-size: 25px; font-weight: 400; letter-spacing: 1px; color: var(--ink); white-space: nowrap; }
  .divider {
    position: absolute; left: 40px; top: 214px;
    width: 530px; height: 5px; background: var(--green);
  }
  .contacts { position: absolute; left: 66px; top: 262px; list-style: none; }
  .contact { display: flex; align-items: center; gap: 26px; height: 104px; }
  .contact-icon { width: 44px; height: 44px; flex: none; }
  .contact-text { font-size: 23px; line-height: 1.4; color: var(--muted); letter-spacing: .5px; white-space: nowrap; }
  .brand {
    position: absolute; left: 540px; top: 382px;
    display: flex; align-items: center; gap: 16px;
    white-space: nowrap;
  }
  .brand-dot { width: 46px; height: 46px; border-radius: 50%; background: var(--green); flex: none; }
  .brand-name { font-size: 46px; font-weight: 500; color: var(--navy); letter-spacing: 2px; text-transform: uppercase; line-height: 1; }
</style>
</head>
<body>
  <section class="card">
    <div class="holder">
      <svg class="holder-icon" viewBox="0 0 56 56" aria-hidden="true">
        <circle cx="28" cy="28" r="28" fill="var(--navy)"/>
        <circle cx="28" cy="22" r="8" fill="#fff"/>
        <path d="M14 42c2-9 8-12 14-12s12 3 14 12z" fill="#fff"/>
      </svg>
      <div>
        <p class="holder-name">Marcus Pellowe</p>
        <p class="holder-title">Managing Director</p>
      </div>
    </div>
    <div class="divider"></div>

    <ul class="contacts">
      <li class="contact">
        <svg class="contact-icon" viewBox="0 0 44 44" aria-hidden="true">
          <rect width="44" height="44" rx="12" fill="var(--green)"/>
          <rect x="15" y="9" width="14" height="26" rx="3" fill="none" stroke="#fff" stroke-width="2.5"/>
          <circle cx="22" cy="31" r="1.6" fill="#fff"/>
        </svg>
        <p class="contact-text">555 014 2273<br>555 014 2274</p>
      </li>
      <li class="contact">
        <svg class="contact-icon" viewBox="0 0 44 44" aria-hidden="true">
          <rect width="44" height="44" rx="12" fill="var(--green)"/>
          <rect x="10" y="12" width="24" height="16" rx="2" fill="none" stroke="#fff" stroke-width="2.5"/>
          <path d="M17 33h10M22 28v5" stroke="#fff" stroke-width="2.5"/>
        </svg>
        <p class="contact-text">marcusp@torvikgroup.example<br>torvikgroup.example</p>
      </li>
      <li class="contact">
        <svg class="contact-icon" viewBox="0 0 44 44" aria-hidden="true">
          <circle cx="22" cy="22" r="22" fill="var(--green)"/>
          <path d="M22 34s-8-9-8-15a8 8 0 0 1 16 0c0 6-8 15-8 15z" fill="#fff"/>
          <circle cx="22" cy="19" r="3" fill="var(--green)"/>
        </svg>
        <p class="contact-text">418 West Orchard Ave<br>Suite 312 Brenham TX</p>
      </li>
    </ul>

    <div class="brand">
      <span class="brand-dot"></span>
      <span class="brand-name">Torvik Group</span>
    </div>
  </section>
</body>
</html>
```